Elegant invitation for prestigious fund raising event

Background
The Lanterns of Grace is a very prestigious fund raising event. It is a sit down dinner, gala type evening with a presentation and auction.
There are three of these event being held at venues around western North Carolina. The areas where these are being held all have one thing in common, they are in the Appalachian Mountains and the craft of quilt making. As you will see from the Concept Boards attached why a mountain theme and quilt “design feel” is being used. One very important point - we don’t want this design to look like an actual quilt.

See the concept board on page 4, which we can’t use that is from another artist but is one good interpretation of the idea and one way to stylize the picture with a “quilt” interpretation and feel. We do not want a literal quilt representation but are looking for an artistic way on how best to interpret what the quilt represents - the feel of “stitching together” the different things across our region that make us all unique but yet bind us all as one.

The Brief:
We want to develop an elegant invitation for these events.
We have develop as save the date (attached) and all we want to use of this is the wording “Lanterns of Grace” we do not like the icon above it.
Also attached is the wording for the invitation, along with the new picture we want to use (taken from the inspiration boards)

Size, fold, color and paper:

Around 5x7 inches, but open to any dimension if you have an idea that will work in a totally different size. Ideally try and stick to something that will fit a standard envelope so that we don’t need to make a special envelope

Fold – up to you if it has a fold or not and which way it folds. Our thought is that it will need a fold to keep it up market but open to any suggestions.
We are happy to print this on a textured paper if you have suggestions. It will be professionally digital printed so the paper needs to be suitable for digital printing

Color. The inspiration boards show the color palette. We have started out in the save the dates with the navy with reversed out white but again totally up to you to use anything from that color palette.
Updates

Target Market(s)

Up market, around 50 - 65 years old, many are retired, very wealthy

Industry/Entity Type

Event

Requirements
Must have
• See brief attached
Nice to have
• See brief attached
Should not have
• See brief attached

```html
<!DOCTYPE html>
<html lang="en">
<head>
<meta charset="utf-8">
<title>Lanterns of Grace — Invitation</title>
<link href="https://fonts.googleapis.com/css2?family=Roboto:wght@300&display=swap" rel="stylesheet">
<style>
  :root {
    --navy: #1c1a44;
    --white: #ffffff;
    --sky-pale: #cdbf9e;
    --sky-gold: #f5c95a;
    --sky-orange: #ee8a3a;
    --mist-blue: #8fa3bc;
    --ridge-slate: #5d7286;
    --forest-olive: #6b7436;
    --forest-deep: #2f3a22;
  }
  html, body {
    margin: 0;
    padding: 0;
    width: 857px;
    height: 1200px;
    overflow: hidden;
    background: var(--navy);
  }
  .card {
    position: relative;
    width: 857px;
    height: 1200px;
    overflow: hidden;
    font-family: "Roboto", Arial, sans-serif;
    font-weight: 300;
    color: var(--white);
  }
  .card__back {
    position: absolute;
    top: 0;
    left: 0;
    width: 857px;
    height: 598px;
    background: var(--navy);
  }
  .brand {
    position: absolute;
    top: 88px;
    left: 0;
    width: 857px;
    display: flex;
    justify-content: center;
    align-items: center;
    gap: 12px;
    transform: rotate(180deg);
    letter-spacing: 0.06em;
  }
  .brand__mark {
    width: 22px;
    height: 22px;
    background: var(--white);
  }
  .brand__name {
    font-size: 21px;
    line-height: 1.05;
    text-transform: uppercase;
    text-align: left;
  }
  .card__front {
    position: absolute;
    top: 598px;
    left: 0;
    width: 857px;
    height: 602px;
  }
  .scene {
    position: absolute;
    inset: 0;
    background:
      linear-gradient(100deg, rgba(47,58,34,0.95) 0%, rgba(107,116,54,0.85) 30%, rgba(107,116,54,0) 55%),
      linear-gradient(180deg,
        var(--sky-pale) 0%,
        var(--sky-gold) 18%,
        var(--sky-orange) 36%,
        var(--mist-blue) 50%,
        var(--ridge-slate) 72%,
        var(--forest-olive) 100%);
  }
  .title {
    position: absolute;
    left: 0;
    width: 857px;
    top: 218px;
    text-align: center;
    margin: 0;
    font-weight: 300;
    line-height: 1;
  }
  .title__lead {
    display: block;
    font-size: 50px;
    letter-spacing: 0.06em;
  }
  .title__main {
    display: block;
    font-size: 118px;
    margin-top: 4px;
    letter-spacing: 0.01em;
  }
</style>
</head>
<body>
  <main class="card">
    <section class="card__back">
      <div class="brand">
        <span class="brand__mark"></span>
        <span class="brand__name">Ridgeview Valley<br>Hospital</span>
      </div>
    </section>
    <section class="card__front">
      <div class="scene" role="img" aria-label="Painted Appalachian mountain landscape at sunset: layered blue misty ridges, orange and gold sky, dark pine trees on a green slope"></div>
      <h1 class="title">
        <span class="title__lead">LANTERNS OF</span>
        <span class="title__main">GRACE</span>
      </h1>
    </section>
  </main>
</body>
</html>
```